Pipeline management & construction company needs nice brochure

Red Mesa Engineering & Construction, LLC (www.redmesaec.example) is a company focused on the midstream oil and gas / pipeline business. We plan, route, design, manage, and construction pipelines and related facilities. We need a brochure to summarize our services as well as give a brief listing of projects completed/desired.

Industry/Entity Type

Construction

Font styles to use
Serif

```html
<!DOCTYPE html>
<html lang="en">
<head>
<meta charset="utf-8">
<title>RMEC Approach – Red Mesa Engineering &amp; Construction</title>
<link rel="stylesheet" href="https://fonts.googleapis.com/css2?family=Libre+Baskerville:ital,wght@0,400;1,400&family=Lato:wght@400&display=swap">
<style>
  :root {
    --backdrop: #c8c8c8;
    --paper: #ffffff;
    --ink: #3b3b3b;
    --ink-dark: #1e1e1e;
    --gold: #d6ae2f;
  }
  * { box-sizing: border-box; margin: 0; padding: 0; }
  html, body {
    width: 1200px; height: 927px; overflow: hidden;
    background: var(--backdrop);
  }
  .canvas {
    position: relative; width: 1200px; height: 927px;
    background: radial-gradient(ellipse at center, #d4d4d4 0%, var(--backdrop) 70%);
  }
  .page {
    position: absolute; left: 260px; top: 24px;
    width: 680px; height: 880px;
    background: var(--paper);
    box-shadow: 0 6px 24px rgba(0,0,0,0.18);
    font-family: "Libre Baskerville", Georgia, serif;
    color: var(--ink);
  }
  .brand {
    display: flex; align-items: center; gap: 8px;
    font-family: "Libre Baskerville", Georgia, serif;
    color: var(--ink-dark);
  }
  .brand-mark {
    width: 26px; height: 26px; border-radius: 50%;
    background: var(--gold); flex: none;
  }
  .brand-name { font-size: 14px; line-height: 1.2; }
  .brand--header { position: absolute; left: 38px; top: 40px; }
  .title {
    position: absolute; left: 88px; top: 118px;
    font-weight: 400; font-size: 32px; color: var(--gold);
  }
  .approach-text {
    position: absolute; left: 88px; top: 200px; width: 312px;
    font-size: 11.5px; line-height: 1.42; text-align: justify;
  }
  .approach-text p + p { margin-top: 14px; }
  .approach-text em { font-style: italic; }
  .contact {
    position: absolute; left: 420px; top: 560px; width: 240px;
  }
  .contact .brand-name { font-size: 13px; }
  .contact-list {
    list-style: none; margin-top: 22px;
    font-family: "Lato", Arial, sans-serif; font-size: 15px;
    color: var(--ink); line-height: 1.4;
  }
  .contact-list li { display: flex; gap: 6px; align-items: flex-start; }
  .contact-list svg { flex: none; margin-top: 4px; }
  .website {
    margin-top: 46px;
    font-family: "Lato", Arial, sans-serif; font-size: 16px;
    color: var(--gold);
  }
</style>
</head>
<body>
<div class="canvas">
  <article class="page">
    <header class="brand brand--header">
      <span class="brand-mark"></span>
      <span class="brand-name">Red Mesa Engineering &amp; Construction, LLC</span>
    </header>

    <h1 class="title">RMEC Approach</h1>

    <section class="approach-text">
      <p>Our services include project management, design, construction, construction management, and Lump Sum-Turn Key/EPC projects.</p>
      <p>By offering all of these services under one banner we feel we can react quickly to the needs of our customers, which is a must in the current market with so many private equity firms and large companies chasing the new hot beds of activity, Shale Plays.</p>
      <p>Our approach to these types of projects will be different than many of our industry peers. We intend to plan the work with the construction in mind. It sounds cliché but “plan your work and work your plan” is appropriate when it comes to pipeline and facilities projects.</p>
      <p><em>Red Mesa Engineering &amp; Construction, LLC</em> (RMEC) is of the belief that every minute of proper planning can save valuable time and capital dollars. One too many HDDs, a fitting in the wrong location, or forgetting to consider elevation changes when planning a hydrotest can greatly impact the outcome of a project.</p>
      <p>With our team of construction focused professionals we plan to direct the design efforts toward streamlining the field construction. Construction is typically the largest portion of most AFE budgets, but sadly it is usually an afterthought, with little attention given to constructability, contract language and unit pricing methodology, or how to select the ideal construction contractor for the type of project being designed.</p>
      <p>With that in mind, we feel that if the proper attention is given to that area early on in the planning process, then we can save our customers unnecessary headaches and wasted dollars once construction is underway.</p>
    </section>

    <footer class="contact">
      <div class="brand">
        <span class="brand-mark"></span>
        <span class="brand-name">Red Mesa Engineering &amp; Construction, LLC</span>
      </div>
      <ul class="contact-list">
        <li>
          <svg width="13" height="12" viewBox="0 0 13 12" aria-hidden="true"><path d="M6.5 0 L13 6 H11 V12 H8 V8 H5 V12 H2 V6 H0 Z" fill="var(--gold)"/></svg>
          <span>4100 County Road 212<br>Mesa Verde, TX 78999</span>
        </li>
        <li>
          <svg width="12" height="12" viewBox="0 0 12 12" aria-hidden="true"><path d="M2.4 0.5 L4.4 2.8 L3.3 4.3 C4 5.8 6 7.8 7.6 8.6 L9.1 7.5 L11.5 9.5 L10.2 11.4 C5.5 11.2 0.8 6.5 0.5 1.8 Z" fill="var(--gold)"/></svg>
          <span>555 014 2290</span>
        </li>
      </ul>
      <p class="website">www.redmesaec.example</p>
    </footer>
  </article>
</div>
</body>
</html>
```